Cause bitches need love too!

I am creating an ad campaign. It will be a series of featured dogs in our shelter and they will contain a picture of the dog wich should be big enough to see on a yard sign and will change every week. I am placing the signs so that they lead you to the shelter. This is why I am also including the copy that says "you're almost there".

I have 4 tag lines:

1. Find unconditional Love.
2. She'll Love you furever!
3. He'll always listen.
4. Meet your new BFF

You're almost there 318 W Harrowgate Ln
Open 10 - 7/Tues-Sat

The dimensions for the sign are 24" wide and 18" high

Every week we will have a different picture of a different dog (hopefully last week's dog gets adopted). Anyhow, I am printing out yard signs, meaning that instead of printing 160 different signs it would be ideal just to replace the photo. So far the copy that is permanent is: "You're almost there. 318 W. Harrowgate Ln."

I could silhouette the image of the dog as well and super impose it on the sign, that's also a consideration, but ideally if I could have 4 tag lines I could print 40 signs of each and just replace the photo manually each week from my printer that would save costs.
Updates

Not enough designs to chose from and I edited the brief and committed to pay no matter what to increase the amount of designs as per your suggestions.

Target Market(s)

Animal lovers

Industry/Entity Type

Campaign

Font styles to use
Sans Serif

Colors

Designer to choose colors to be used in the design.

Requirements
Must have
• The dimensions for the sign are 24" wide and 18" high
Nice to have
• I want the signs to be hip, they should have a positive feel to them. You can alter the photos if you like. I am even open to new copy if you think something else works better.

```html
<!DOCTYPE html>
<html lang="en">
<head>
<meta charset="utf-8">
<title>Shelter Yard Sign Concepts</title>
<link rel="stylesheet" href="https://fonts.googleapis.com/css2?family=Alegreya:wght@700&family=Great+Vibes&family=Cabin+Sketch:wght@400;700&family=Rubik+Dirt&family=Montserrat:wght@400;700&display=swap">
<style>
  :root {
    --stage: #8c8f93;
    --label-gold: #e9c98a;
    --label-dark: #231a14;
    --plum-dark: #3a1424;
    --plum-mid: #7a3c52;
    --plum-glow: #c58a9c;
    --cream: #f6eaa8;
    --white: #f4f1ea;
    --smoke-dark: #1d1b1f;
    --smoke-light: #c9c3bf;
    --gold: #f0c063;
    --yellow: #f2ec1a;
    --dog-tan: #b98a4e;
    --dog-dark: #3a2a1c;
  }
  * { box-sizing: border-box; margin: 0; padding: 0; }
  html, body { width: 1200px; height: 1200px; overflow: hidden; }
  body { background: var(--stage); position: relative; font-family: "Montserrat", sans-serif; }

  .sign { position: absolute; width: 520px; height: 390px; overflow: hidden; }
  .sign--forever { left: 40px; top: 40px;
    background: radial-gradient(ellipse at 60% 40%, var(--plum-glow) 0%, var(--plum-mid) 45%, var(--plum-dark) 100%); }
  .sign--sketch { left: 640px; top: 400px;
    background: radial-gradient(ellipse at 65% 45%, var(--smoke-light) 0%, #6d6460 40%, var(--smoke-dark) 85%); }
  .sign--script { left: 40px; top: 770px;
    background: radial-gradient(ellipse at 62% 45%, var(--smoke-light) 0%, #6d6460 40%, var(--smoke-dark) 85%); }

  .dog-photo { position: absolute; left: 0; bottom: 0; width: 300px; height: 370px;
    border-radius: 45% 55% 0 0 / 40% 40% 0 0;
    background: radial-gradient(ellipse at 55% 35%, var(--dog-tan) 0%, #8a6236 50%, var(--dog-dark) 100%); }
  .ember-glow { position: absolute; left: 240px; right: 0; bottom: 0; height: 90px;
    background: linear-gradient(180deg, transparent, rgba(178,64,29,.55) 55%, rgba(40,20,15,.9)); }
  .petal-heart { position: absolute; left: 400px; top: 300px; width: 110px; height: 60px;
    background: radial-gradient(ellipse, #b2263e 0%, rgba(120,20,40,0) 70%); }

  .tagline { position: absolute; text-align: center; white-space: nowrap; font-weight: 400; }
  .sign--forever .tagline { left: 280px; top: 70px; width: 220px; color: var(--cream); }
  .serif-line { font-family: "Alegreya", serif; font-weight: 700; font-size: 44px; line-height: 1; }
  .script-line { font-family: "Great Vibes", cursive; font-size: 58px; line-height: 1; }

  .sign--sketch .tagline { left: 300px; top: 70px; text-align: left; color: var(--white);
    font-family: "Cabin Sketch", sans-serif; }
  .sketch-small { font-size: 31px; line-height: 1.1; }
  .sketch-big { font-size: 72px; font-weight: 700; line-height: 1; }

  .sign--script .tagline { left: 268px; top: 100px; width: 236px; }
  .dirt-line { font-family: "Rubik Dirt", sans-serif; color: var(--white); font-size: 22px; line-height: 1.2; }
  .sign--script .script-line { color: var(--yellow); font-size: 62px; margin-top: -4px; display: inline-block; }

  .directions { position: absolute; left: 310px; bottom: 40px; width: 185px; }
  .directions p { font-size: 11px; color: var(--white); line-height: 1.35; }
  .hours { margin-top: 8px; padding: 4px 0; border-top: 1.5px solid var(--white); border-bottom: 1.5px solid var(--white);
    font-size: 12px; font-weight: 700; letter-spacing: 1px; color: var(--white); }
  .sign--sketch .hours, .sign--script .hours { color: var(--gold); }

  .concept-label { position: absolute; font-size: 44px; font-weight: 400; }
  .concept-label--one { left: 620px; top: 190px; color: var(--label-gold); }
  .concept-label--two { left: 350px; top: 560px; color: var(--label-dark); }
  .concept-label--three { left: 640px; top: 940px; color: var(--label-gold); }
</style>
</head>
<body>
  <section class="sign sign--forever">
    <div class="dog-photo" role="img" aria-label="Portrait photo of the featured shelter dog, a tan and black mixed breed"></div>
    <div class="petal-heart" role="img" aria-label="Heart made of red rose petals"></div>
    <h1 class="tagline">
      <span class="serif-line">She'll</span><br>
      <span class="script-line">Love You</span><br>
      <span class="serif-line">forever!</span>
    </h1>
    <div class="directions">
      <p>You're almost there<br>318 W Harrowgate Ln</p>
      <div class="hours">OPEN 10 - 7/TUES-SAT</div>
    </div>
  </section>
  <div class="concept-label concept-label--one">Design 1</div>

  <div class="concept-label concept-label--two">Design 2</div>
  <section class="sign sign--sketch">
    <div class="ember-glow"></div>
    <div class="dog-photo" role="img" aria-label="Portrait photo of the featured shelter dog, a tan and black mixed breed"></div>
    <h1 class="tagline">
      <span class="sketch-small">Find</span><br>
      <span class="sketch-small">unconditional</span><br>
      <span class="sketch-big">LOVE</span>
    </h1>
    <div class="directions">
      <p>You're almost there<br>318 W Harrowgate Ln</p>
      <div class="hours">OPEN 10 - 7/TUES-SAT</div>
    </div>
  </section>

  <section class="sign sign--script">
    <div class="ember-glow"></div>
    <div class="dog-photo" role="img" aria-label="Portrait photo of the featured shelter dog, a tan and black mixed breed"></div>
    <h1 class="tagline">
      <span class="dirt-line">FIND<br>UNCONDITIONAL</span><br>
      <span class="script-line">Love</span>
    </h1>
    <div class="directions">
      <p>You're almost there<br>318 W Harrowgate Ln</p>
      <div class="hours">OPEN 10 - 7/TUES-SAT</div>
    </div>
  </section>
  <div class="concept-label concept-label--three">Design 3</div>
</body>
</html>
```